Business card design for my trucking company

I would like a business card designed for my new trucking company. Please use my logo. the rest of the design is up to you. i would like my clients to say wow when they see the card. Im looking forward to seeing your designs

Target Market(s)

Industry/Entity Type

Trucking Company

Contact Information for Business Card

Marcus Tillbrook President
518-555-0147
ridgelinehaulingcompany@postvane.com

Font styles to use
Serif

Requirements
Must have
• my logo, name and number. we are located in Schenectady New York. the rest is up to you
Nice to have
• up to you
Should not have
• none

```html
<!DOCTYPE html>
<html lang="en">
<head>
<meta charset="utf-8">
<title>Ridgeline Hauling &amp; Logistics – Business Card</title>
<link rel="stylesheet" href="https://fonts.googleapis.com/css2?family=Open+Sans:wght@400;600;800&display=swap">
<style>
  :root {
    --stage: #2b2f35;
    --brand-red: #e02226;
    --deep-red: #c8161b;
    --ink: #121212;
    --paper: #ffffff;
    --soft-white: #e9e9e9;
  }
  * { box-sizing: border-box; margin: 0; padding: 0; }
  html, body { width: 1200px; height: 900px; overflow: hidden; }
  body {
    background: var(--stage);
    font-family: "Open Sans", Arial, sans-serif;
    position: relative;
  }
  .card {
    position: absolute;
    width: 560px;
    height: 320px;
    border-radius: 22px;
    overflow: hidden;
    box-shadow: 0 18px 40px rgba(0,0,0,.45);
  }
  /* Front: red */
  .card-front { left: 580px; top: 110px; background: var(--brand-red); }
  .card-front .map-area {
    position: absolute; left: 90px; top: 30px; width: 400px; height: 260px;
    background: radial-gradient(ellipse at center, rgba(160,10,14,.35), rgba(160,10,14,0) 70%);
  }
  .wordmark { font-weight: 800; line-height: 1; }
  .card-front .brand {
    position: absolute; left: 0; right: 0; top: 118px; text-align: center; color: var(--paper);
  }
  .card-front .brand-name { font-size: 54px; letter-spacing: 1px; }
  .card-front .brand-sub { font-size: 15px; letter-spacing: 3px; margin-top: 8px; }

  /* Back: white / black */
  .card-back { left: 60px; top: 470px; background: var(--ink); }
  .card-back svg.curve { position: absolute; inset: 0; }
  .card-back .logo-block {
    position: absolute; left: 22px; top: 112px; width: 220px; color: var(--brand-red);
  }
  .card-back .logo-block .brand-name { font-size: 30px; }
  .card-back .logo-block .brand-sub { font-size: 8.5px; letter-spacing: 1.5px; margin-top: 5px; }

  .details {
    position: absolute; right: 28px; top: 30px; width: 290px; text-align: right; color: var(--paper);
  }
  .details .brand-name { font-size: 34px; color: var(--brand-red); }
  .details .brand-sub { font-size: 10px; letter-spacing: 2px; margin-top: 5px; }
  .person { margin-top: 20px; }
  .person-name { font-size: 21px; font-weight: 600; }
  .person-name .first { color: var(--brand-red); font-weight: 400; }
  .person-title { font-size: 13px; color: var(--soft-white); }
  .address { margin-top: 14px; font-size: 13px; line-height: 1.35; color: var(--soft-white); }
  .contacts { list-style: none; margin-top: 12px; font-size: 12px; line-height: 1.55; color: var(--soft-white); }
  .contacts li { display: flex; justify-content: flex-end; align-items: center; gap: 7px; }
  .contacts svg { width: 10px; height: 10px; fill: var(--brand-red); flex: none; }
</style>
</head>
<body>

<section class="card card-front">
  <div class="map-area" role="img" aria-label="Faint dotted world map texture"></div>
  <div class="brand">
    <div class="wordmark brand-name">RIDGELINE</div>
    <div class="wordmark brand-sub">HAULING &amp; LOGISTICS INC.</div>
  </div>
</section>

<section class="card card-back">
  <svg class="curve" viewBox="0 0 560 320" width="560" height="320" aria-hidden="true">
    <path d="M0,0 H272 C250,170 200,280 80,320 H0 Z" fill="var(--brand-red)"/>
    <path d="M0,0 H254 C232,160 180,262 62,300 C40,308 20,312 0,314 Z" fill="var(--paper)"/>
  </svg>
  <div class="logo-block">
    <div class="wordmark brand-name">RIDGELINE</div>
    <div class="wordmark brand-sub">HAULING &amp; LOGISTICS INC.</div>
  </div>
  <div class="details">
    <div class="wordmark brand-name">RIDGELINE</div>
    <div class="wordmark brand-sub">HAULING &amp; LOGISTICS INC.</div>
    <div class="person">
      <div class="person-name"><span class="first">Marcus</span> Tillbrook</div>
      <div class="person-title">President</div>
    </div>
    <div class="address">1420 Kestrel Avenue,<br>Suite 17-21.</div>
    <ul class="contacts">
      <li>518-555-0147
        <svg viewBox="0 0 10 10"><path d="M2 0 L4 2.5 L3 3.8 Q4.5 6 6.2 7 L7.5 6 L10 8 L8.5 10 Q3 9 0 1.5 Z"/></svg></li>
      <li>ridgelinehaulingcompany@postvane.com
        <svg viewBox="0 0 10 10"><path d="M0 2 H10 V8 H0 Z M0.6 2.4 L5 5.6 L9.4 2.4" stroke="var(--ink)" stroke-width="0.8"/></svg></li>
      <li>www.ridgelinehaulingcompany.com
        <svg viewBox="0 0 10 10"><circle cx="5" cy="5" r="5"/></svg></li>
    </ul>
  </div>
</section>

</body>
</html>
```